Agriculture Technology Website Design Project

We need a new website for a company called Brook Ledger Works. We have a document laid out with all of the requirements (see below) and would like you to follow the instructions on there. In this document, there is all of the copy that must be included on the website and what order it should go in as well as images. These images have specific names and are listed in the document as to where they should go. Please make this one continuous site that users can easily scroll through. We would like it to be sleek and modern with as little clutter as possible. Please refer to the brochure that we have posted below (Stone Analytica.pdf) for a design we have had done for the company in the past. We really like this design and it would be great if the color scheme was similar on the website.

Industry/Entity Type

Agriculture

Number of Pages Required

1 page

Font styles to use
Sans Serif

```html
<!DOCTYPE html>
<html lang="en">
<head>
<meta charset="utf-8">
<title>Brook Ledger Works</title>
<link rel="stylesheet" href="https://fonts.googleapis.com/css2?family=Arimo:wght@400;700&family=Raleway:wght@300;400;500&family=Cormorant+Garamond:ital,wght@1,500&family=Josefin+Sans:wght@300&display=swap">
<style>
  :root {
    --white: #ffffff;
    --ink: #111111;
    --green: #3f7d63;
    --green-soft: #82ad8f;
    --nav-active: #ece9e4;
    --nav-text: #3a3a3a;
    --brand-blue: #2a6fb3;
  }
  * { margin: 0; padding: 0; box-sizing: border-box; }
  html, body { width: 1158px; height: 1200px; overflow: hidden; background: var(--white); }
  body { position: relative; font-family: "Raleway", sans-serif; color: var(--ink); }
  .abs { position: absolute; }
  .center { left: 0; width: 1158px; text-align: center; }

  /* Header */
  .site-header { top: 0; left: 0; width: 1158px; height: 60px; background: var(--white); border-bottom: 1px solid #e6e6e6; }
  .brand { left: 352px; top: 22px; display: flex; align-items: center; gap: 4px; font-family: "Arimo", sans-serif; font-weight: 700; font-size: 9px; color: var(--green); }
  .brand-mark { width: 8px; height: 8px; background: var(--green); }
  .main-nav { left: 595px; top: 30px; display: flex; font-family: "Arimo", sans-serif; font-size: 7px; color: var(--nav-text); }
  .main-nav span { display: block; height: 22px; line-height: 22px; padding: 0 7px; }
  .main-nav .active { background: var(--nav-active); }

  /* Hero */
  .hero { top: 60px; left: 0; width: 1158px; height: 256px;
    background: linear-gradient(180deg, #3e3324 0%, #5a4a34 45%, #625b3a 68%, #5f8a2c 82%, #6f9a34 100%); }
  .hero-title { top: 152px; font-family: "Arimo", sans-serif; font-weight: 700; font-size: 28px; letter-spacing: 3.5px; color: var(--white); }
  .hero-sub { top: 192px; font-size: 12px; color: var(--white); font-weight: 400; }
  .scroll-down { font-family: "Cormorant Garamond", serif; font-style: italic; font-size: 11px; letter-spacing: 1px; color: var(--white); }
  .scroll-down.u { text-decoration: underline; }

  /* Services */
  .service { top: 340px; width: 130px; text-align: center; color: var(--green); }
  .service h3 { font-weight: 400; font-size: 11px; line-height: 13.5px; text-transform: uppercase; }
  .service p { font-family: "Josefin Sans", sans-serif; font-size: 6px; line-height: 11px; margin: 2px auto 0; width: 92px; color: #2f5f4a; }
  .btn { width: 63px; height: 18px; line-height: 17px; border: 1px solid var(--green); font-size: 6.5px; color: var(--green); text-align: center; letter-spacing: -0.2px; }

  /* Goal */
  .goal { top: 485px; left: 0; width: 1158px; height: 298px;
    background: linear-gradient(180deg, #545a56 0%, #6c7064 22%, #b39a55 42%, #c6a548 65%, #b8953c 100%); }
  .goal-kicker { top: 520px; font-family: "Arimo", sans-serif; font-size: 18px; letter-spacing: 2.6px; line-height: 21px; color: var(--white); }
  .goal-title { top: 574px; font-family: "Arimo", sans-serif; font-weight: 700; font-size: 27px; letter-spacing: 3px; color: var(--white); }
  .goal-body { top: 615px; left: 358px; width: 444px; text-align: center; font-size: 12.3px; line-height: 16.5px; color: var(--white); }

  /* Why */
  .why-title { top: 806px; font-family: "Arimo", sans-serif; font-weight: 700; font-size: 31px; letter-spacing: 6px; color: var(--ink); }
  .why-sub { top: 854px; font-family: "Arimo", sans-serif; font-weight: 700; font-size: 9px; letter-spacing: 0.6px; }
  .why-body { top: 877px; font-size: 8.6px; line-height: 22.6px; color: #222; }

  /* Products */
  .products { top: 971px; left: 0; width: 1158px; height: 229px;
    background: linear-gradient(180deg, #1f2a24 0%, #4a4a30 35%, #9b7f4c 70%, #c4a46c 100%); }
  .products-title { top: 996px; font-family: "Arimo", sans-serif; font-weight: 700; font-size: 22px; letter-spacing: 4px; color: var(--white); }
  .product-card { top: 1038px; left: 356px; width: 448px; height: 130px; background: var(--white); text-align: center; }
  .product-card h4 { margin-top: 14px; font-family: "Arimo", sans-serif; font-weight: 700; font-size: 17px; color: var(--green-soft); }
  .product-card p { margin: 6px auto 0; width: 380px; font-size: 6.8px; line-height: 12px; color: var(--green); }
  .product-brand { margin-top: 12px; display: inline-flex; align-items: center; gap: 5px; font-size: 13px; color: var(--brand-blue); }
  .product-brand i { display: block; width: 9px; height: 9px; background: var(--brand-blue); }
</style>
</head>
<body>
  <header class="abs site-header">
    <div class="abs brand"><span class="brand-mark"></span>Brook Ledger Works</div>
    <nav class="abs main-nav">
      <span class="active">HOME</span><span>About Us</span><span>Why BLW?</span><span>Products</span><span>Contact Us</span>
    </nav>
  </header>

  <section class="abs hero" role="img" aria-label="Photo of a tractor working a green field in light rain"></section>
  <h1 class="abs center hero-title">Brook Ledger Works</h1>
  <p class="abs center hero-sub">Bringing industrial automation to the farm</p>
  <p class="abs center scroll-down u" style="top:273px">Scroll Down</p>
  <svg class="abs" style="left:573px;top:297px" width="12" height="8" viewBox="0 0 12 8"><path d="M1 1l5 5 5-5" fill="none" stroke="#fff" stroke-width="1.5"/></svg>

  <div class="abs service" style="left:80px"><h3>Crop<br>Monitoring</h3><p>Ensuring that you have real-time information to optimize irrigation management</p></div>
  <div class="abs btn" style="left:114px;top:434px">Learn More</div>

  <div class="abs service" style="left:298px"><h3>Pump<br>Monitoring<br>and Control</h3><p>Salable and cost-effective pump monitoring with built-in remote control</p></div>
  <div class="abs btn" style="left:331px;top:436px">Learn More</div>

  <div class="abs service" style="left:515px"><h3>Irrigation<br>Automation</h3><p>Upgrade your irrigation system: from retrofit to ranch-wide automat</p></div>
  <div class="abs btn" style="left:549px;top:435px">Learn More</div>

  <div class="abs service" style="left:733px"><h3>Control Panel<br>Design and<br>Build</h3><p>Leverage BLW design and build expertise to meet your exact needs and specifications</p></div>
  <div class="abs btn" style="left:766px;top:436px">Learn More</div>

  <div class="abs service" style="left:950px"><h3>Contact Us</h3><p style="width:100px">For immediate support call (555 014 - 2290)</p></div>
  <div class="abs btn" style="left:983px;top:437px">Learn More</div>

  <section class="abs goal" role="img" aria-label="Photo of a golden harvested field with hay bales under a stormy sky"></section>
  <p class="abs center goal-kicker">OUR GOAL: to be your trusted partner for<br>technology adoption</p>
  <h2 class="abs center goal-title">BLW is a Systems Integrator</h2>
  <p class="abs goal-body">Text: Our focus is on helping California growers design, build and adopt effective irrigation management solutions. Our team has worked together for over 15 years, providing monitoring and control systems for 60+ crops that have successfully helped over 500 farms significantly improve irrigation management. We also farm our own 200 acre technology lab to help ensure we deliver reliable monitoring and automation to your farm.</p>
  <p class="abs center scroll-down" style="top:740px">Scroll Down</p>
  <svg class="abs" style="left:573px;top:765px" width="12" height="8" viewBox="0 0 12 8"><path d="M1 1l5 5 5-5" fill="none" stroke="#fff" stroke-width="1.5"/></svg>

  <h2 class="abs center why-title">WHY BLW?</h2>
  <p class="abs center why-sub">We're your local farm data team.</p>
  <p class="abs center why-body">We are experts at deploying Information Technology for irrigation<br>management.We partner with our customers to deliver the right<br>solutions.Everything we sell is off-the-shelf, cost-effective and reliable.</p>

  <section class="abs products" role="img" aria-label="Photo of ripe wheat ears against a dark background"></section>
  <h2 class="abs center products-title">PRODUCTS</h2>
  <div class="abs product-card">
    <h4>Stone Analytica</h4>
    <p>Stone Analytica is a cost-effective suite of tools built by Brook Ledger Works for irrigation management, providing farmers access to state-of-the-art industrial monitoring and control tools already widely adopted in other industries.</p>
    <div class="product-brand"><i></i>Stone Analytica</div>
  </div>
</body>
</html>
```